Design 1 form and 3 panels for shopping App

This goal of this project is to enhance the design of our “internal shopping” web application. We call it “qOrderly”. qOrderly allows an employee to requisition material or services. The user fills a shopping cart and “checks out” in a manner similar to Brivanto or any other consumer site.
The task is to redesign the main shopping form and three “pull out” panels. We are looking for a clean, contemporary design consistent with our branding. Our goal is to make the shopping experience as close as possible to what a user experiences on consumer sites (e.g. Brivanto, Clovane, Farrow Yard). A new user should be able to shop and check out without any training. Therefore, it is important that the shopping experience be familiar to the user.
Updates

Project Deadline Extended
Reason: Have not yet received a complete design (including panels)

Target Market(s)

Mid to large sized companies (> 50M USD Sales per Year)

Industry/Entity Type

Shopping

Number of Pages Required

4 page

Requirements
Must have
• Must look good in the current menu frame.

```html
<!DOCTYPE html>
<html lang="en">
<head>
<meta charset="utf-8">
<title>qOrderly – Request Material</title>
<link rel="stylesheet" href="https://fonts.googleapis.com/css2?family=Questrial&display=swap">
<style>
:root{
  --black:#050505;
  --white:#ffffff;
  --green:#7dc34c;
  --green-dark:#6ab33a;
  --orange:#fb7c53;
  --grey-band:#f1f1f1;
  --tab-grey:#f4f4f4;
  --border:#e4e4e4;
  --text:#3a3a3a;
  --muted:#8a8a8a;
  --brand-blue:#1f5fae;
  --footer:#161616;
  --footer-top:#0c0c0c;
}
*{box-sizing:border-box;margin:0;padding:0}
html,body{width:1144px;height:1200px;overflow:hidden;background:var(--white)}
body{font-family:"Questrial",sans-serif;color:var(--text);position:relative}
.abs{position:absolute}

/* top bar */
.topbar{left:0;top:0;width:1144px;height:38px;background:var(--black);color:var(--white);font-size:12.5px}
.topbar .user{left:93px;top:12px}
.topbar .divider{left:252px;top:0;width:1px;height:38px;background:#333}
.topbar .role{left:264px;top:12px}
.topbar .links{right:93px;top:11px;display:flex;gap:10px}
.topbar .links span.sep{color:#777}
.dot{display:inline-block;width:9px;height:9px;border-radius:50%;border:2px solid var(--white);margin-left:4px;vertical-align:-1px}

/* brand */
.brand{left:829px;top:62px;font-size:38px;color:var(--brand-blue);letter-spacing:1px}

/* tabs */
.tab{top:89px;height:42px;background:var(--tab-grey);border:1px solid var(--border);border-bottom:none;font-size:14px;color:var(--text);display:flex;align-items:center;justify-content:center}
.tab.active{top:82px;height:49px;background:var(--green);color:var(--white);border-color:var(--green)}

/* sub nav */
.subnav{left:0;top:131px;width:1144px;height:45px;background:var(--green);color:var(--white);font-size:14px}
.subnav .items{left:94px;top:0;height:45px;display:flex;align-items:center;gap:18px}
.subnav .bar{width:1px;height:20px;background:rgba(255,255,255,.7)}
.subnav .bullet{width:4px;height:4px;border-radius:50%;background:var(--white)}

/* tool band */
.toolband{left:0;top:176px;width:1144px;height:76px;background:var(--grey-band);border-bottom:1px solid var(--border)}
.btn-drop{top:195px;height:36px;background:var(--orange);color:var(--white);font-size:12.5px;display:flex;align-items:center;justify-content:center;gap:10px}
.caret{width:0;height:0;border-left:5px solid transparent;border-right:5px solid transparent;border-top:6px solid var(--white)}
.badge{position:absolute;width:11px;height:11px;border-radius:50%;background:var(--green);color:var(--white);font-size:7px;text-align:center;line-height:11px;border:1px solid var(--white)}
.search{left:244px;top:195px;width:325px;height:36px;display:flex}
.search .icon{width:43px;background:var(--orange);display:flex;align-items:center;justify-content:center}
.search .field{flex:1;background:var(--white);border:1px solid var(--border);font-size:11.5px;color:#aaa;padding:11px 10px}
.search .plus{width:38px;background:var(--green);display:flex;align-items:center;justify-content:center;color:var(--white);font-size:18px}

/* sections */
.section-title{left:93px;font-size:21px;color:#222;display:flex;align-items:baseline;gap:10px}
.section-title .view{font-size:12px;color:var(--green)}
.rule{height:1px;background:#dcdcdc}
.pager{width:20px;height:19px;border:1px solid #d0d0d0;display:flex;align-items:center;justify-content:center}

.card{width:176px}
.thumb{width:176px;height:176px;border:1px solid var(--border);position:relative}
.thumb .art{position:absolute;left:18px;top:30px;right:18px;bottom:30px;border-radius:6px}
.pname{font-size:12.5px;text-align:center;margin-top:21px;white-space:nowrap}
.price{font-size:13px;color:var(--green-dark);text-align:center;margin-top:11px}
.stock{font-size:11.5px;color:var(--muted);text-align:center;margin-top:13px}
.buy{display:flex;justify-content:center;gap:7px;margin-top:17px}
.qty{width:43px;height:31px;border:1px solid #dcdcdc;font-size:10px;display:flex;align-items:center;justify-content:center}
.addcart{width:94px;height:31px;background:var(--orange);color:var(--white);font-size:10px;display:flex;align-items:center;justify-content:center}
.sale{position:absolute;right:0;top:11px;background:var(--green);color:var(--white);font-size:9.5px;padding:5px 9px}

/* footer */
.newsletter{left:0;top:1052px;width:1144px;height:60px;background:var(--footer-top);color:var(--white)}
.newsletter .label{left:93px;top:20px;font-size:16px}
.newsletter .email{left:203px;top:16px;width:259px;height:30px;background:var(--white);font-size:9.5px;color:#999;padding:9px 11px}
.newsletter .subscribe{left:467px;top:16px;width:85px;height:30px;background:var(--green);font-size:9.5px;display:flex;align-items:center;justify-content:center}
.social{top:16px;width:29px;height:29px;background:#3b3b3b}
.footer{left:0;top:1112px;width:1144px;height:88px;background:var(--footer);color:#cfcfcf;text-align:center}
.footer .links{margin-top:30px;font-size:11px;letter-spacing:.2px}
.footer .copy{margin-top:12px;font-size:11.5px}
</style>
</head>
<body>

<header class="abs topbar">
  <div class="abs user">Logged in As Dana Whitlow <span class="dot"></span></div>
  <div class="abs divider"></div>
  <div class="abs role">Current Role Staff <span class="dot"></span></div>
  <nav class="abs links"><span>Touch</span><span class="sep">|</span><span>New Tab</span><span class="sep">|</span><span>Help</span><span class="sep">|</span><span>Support</span><span class="sep">|</span><span>Logout</span></nav>
</header>

<div class="abs brand">qOrderly</div>

<div class="abs tab" style="left:95px;width:85px">Home</div>
<div class="abs tab active" style="left:181px;width:149px">Request Material</div>
<div class="abs tab" style="left:333px;width:149px">Report Expenses</div>
<div class="abs tab" style="left:485px;width:173px">Approve Documents</div>
<div class="abs tab" style="left:660px;width:53px">
  <svg width="14" height="12" viewBox="0 0 14 12"><path d="M6 1 1 5.5 6 10V7c3 0 5 1 7 4-0.5-4-3-7-7-7z" fill="#333"/></svg>
</div>

<nav class="abs subnav">
  <div class="abs items">
    <span class="bar"></span><span>Enter A Requisition</span><span class="bar"></span>
    <span>OtherTransactions</span><span class="bullet"></span>
    <span>Request History</span><span class="bullet"></span>
    <span>Purchase History</span><span class="bullet"></span>
    <span>Your Profile</span>
  </div>
</nav>

<div class="abs toolband"></div>
<div class="abs btn-drop" style="left:92px;width:113px">CATALOG <span class="caret"></span></div>
<div class="abs search">
  <div class="icon"><svg width="12" height="12" viewBox="0 0 12 12"><circle cx="5" cy="5" r="3.6" fill="none" stroke="#fff" stroke-width="1.8"/><path d="M7.6 7.6 11 11" stroke="#fff" stroke-width="2"/></svg></div>
  <div class="field">Search...</div>
  <div class="plus">+</div>
</div>
<div class="abs btn-drop" style="left:598px;width:131px">
  <span style="position:relative;width:18px;height:22px">
    <svg width="18" height="22" viewBox="0 0 18 22"><rect x="1" y="3" width="15" height="18" fill="none" stroke="#fff" stroke-width="1.6"/><path d="M4 8h3M9 8h4M4 12h3M9 12h4M4 16h3M9 16h4" stroke="#fff" stroke-width="1.6"/></svg>
    <span class="badge" style="left:9px;top:-4px">4</span>
  </span>
  MY LIST <span class="caret"></span></div>
<div class="abs btn-drop" style="left:761px;width:131px">MARKETPLACE <span class="caret"></span></div>
<div class="abs btn-drop" style="left:935px;width:115px">
  <span style="position:relative;width:22px;height:20px">
    <svg width="22" height="20" viewBox="0 0 22 20"><path d="M1 2h3l3 10h11l2-7H6" fill="none" stroke="#fff" stroke-width="1.6"/><circle cx="8" cy="16" r="1.8" fill="#fff"/><circle cx="16" cy="16" r="1.8" fill="#fff"/></svg>
    <span class="badge" style="left:13px;top:-5px">4</span>
  </span>
  CART <span class="caret"></span></div>

<!-- Recent products -->
<div class="abs section-title" style="top:292px">RECENT PRODUCTS <span class="view">( View All )</span></div>
<div class="abs rule" style="left:370px;top:304px;width:627px"></div>
<div class="abs pager" style="left:1005px;top:295px"><svg width="6" height="9"><path d="M5 1 1 4.5 5 8" fill="none" stroke="#555"/></svg></div>
<div class="abs pager" style="left:1030px;top:295px"><svg width="6" height="9"><path d="M1 1 5 4.5 1 8" fill="none" stroke="#555"/></svg></div>

<div class="abs card" style="left:94px;top:343px">
  <div class="thumb"><div class="art" role="img" aria-label="Wooden dining table" style="background:linear-gradient(#f7ecd9,#d9a764)"></div></div>
  <div class="pname">Product Name dolore siire</div><div class="price">$129.99 / Box (200 Each)</div><div class="stock">Not Inventoried</div>
  <div class="buy"><div class="qty">1</div><div class="addcart">ADD TO CART</div></div>
</div>
<div class="abs card" style="left:291px;top:343px">
  <div class="thumb"><div class="art" role="img" aria-label="Open laptop computer" style="background:linear-gradient(#5d8fcf,#9aa0a8)"></div></div>
  <div class="pname">Product Name dolore</div><div class="price">$99.49 Per Foot</div><div class="stock">73 Available</div>
  <div class="buy"><div class="qty">1</div><div class="addcart">ADD TO CART</div></div>
</div>
<div class="abs card" style="left:484px;top:343px">
  <div class="thumb"><div class="art" role="img" aria-label="Office inkjet printer" style="background:linear-gradient(#e9e9e9,#3c3c3c)"></div></div>
  <div class="pname">Product Name dolore siire</div><div class="price">$129.99 / Box (200 Each)</div><div class="stock">Not Inventoried</div>
  <div class="buy"><div class="qty">1</div><div class="addcart">ADD TO CART</div></div>
</div>
<div class="abs card" style="left:681px;top:343px">
  <div class="thumb"><div class="art" role="img" aria-label="Kitchen appliances: fridge, oven and washer" style="background:linear-gradient(#e4e6e8,#8b9096)"></div></div>
  <div class="pname">Product Name dolore</div><div class="price">$99.49 Per Foot</div><div class="stock">Out of Stock</div>
  <div class="buy"><div class="qty">1</div><div class="addcart">ADD TO CART</div></div>
</div>
<div class="abs card" style="left:873px;top:343px">
  <div class="thumb"><div class="art" role="img" aria-label="Round pedestal side table" style="background:linear-gradient(#b0624a,#6b2a1b)"></div></div>
  <div class="pname">Product Name dolore siire</div><div class="price">$99.49 Per Foot</div><div class="stock">73 Available</div>
  <div class="buy"><div class="qty">1</div><div class="addcart">ADD TO CART</div></div>
</div>

<!-- Popular categories -->
<div class="abs section-title" style="top:714px">POPULAR CATEGORIES <span class="view">( View All )</span></div>
<div class="abs rule" style="left:395px;top:726px;width:602px"></div>
<div class="abs pager" style="left:1005px;top:718px"><svg width="6" height="9"><path d="M5 1 1 4.5 5 8" fill="none" stroke="#555"/></svg></div>
<div class="abs pager" style="left:1030px;top:718px"><svg width="6" height="9"><path d="M1 1 5 4.5 1 8" fill="none" stroke="#555"/></svg></div>

<div class="abs card" style="left:94px;top:779px">
  <div class="thumb"><div class="art" role="img" aria-label="Cleaning supplies and vacuum cleaner" style="background:linear-gradient(135deg,#e57ab0,#4aa3dd)"></div></div>
  <div class="pname">Product Name dolore siire</div>
</div>
<div class="abs card" style="left:291px;top:779px">
  <div class="thumb"><div class="art" role="img" aria-label="Desktop printer with paper" style="background:linear-gradient(#3a3a3a,#eeeeee)"></div></div>
  <div class="pname">Product Name dolore</div>
</div>
<div class="abs card" style="left:484px;top:779px">
  <div class="thumb"><div class="art" role="img" aria-label="Binders on a laptop keyboard" style="background:linear-gradient(90deg,#3d6fb6,#d83a3a,#3d6fb6)"></div><span class="sale">SALE</span></div>
  <div class="pname">Product Name dolore siire</div>
</div>
<div class="abs card" style="left:681px;top:779px">
  <div class="thumb"><div class="art" role="img" aria-label="Wooden serving tray" style="background:linear-gradient(#c9844a,#8a4a1e)"></div></div>
  <div class="pname">Product Name dolore</div>
</div>
<div class="abs card" style="left:873px;top:779px">
  <div class="thumb"><div class="art" role="img" aria-label="Janitorial cleaning cart" style="background:linear-gradient(#f2cd2a,#2f63c2)"></div></div>
  <div class="pname">Product Name dolore siire</div>
</div>

<!-- Footer -->
<section class="abs newsletter">
  <div class="abs label">NEWSLETTER</div>
  <div class="abs email">Eami Address</div>
  <div class="abs subscribe">SUBSCRIBE</div>
  <div class="abs social" style="left:787px"></div>
  <div class="abs social" style="left:824px"></div>
  <div class="abs social" style="left:861px"></div>
  <div class="abs social" style="left:898px"></div>
  <div class="abs social" style="left:935px"></div>
  <div class="abs social" style="left:971px"></div>
  <div class="abs social" style="left:1008px"></div>
</section>
<footer class="abs footer">
  <div class="links">MARKETPLACE &nbsp;/&nbsp; CONTACT &nbsp;/&nbsp; TERMS OF SERVICE &nbsp;/&nbsp; PRIVACY POLICY</div>
  <div class="copy">© 2015 &nbsp;qOrderly, All Rights Reserved.</div>
</footer>

</body>
</html>
```